Simple graphic for a book or slide presentation

We are looking for a style that suits the style of our book. It's title is Harbor. Keeping a calm course through stormy seas. There will be more line drawing/graphics in the book but how you design this image will create the style for all the other simple graphics in the book (once we decide what they are). So this one design will lead to a few more to match the style of this one. We'd like the shape of the overall graphic (i.e the arrows and words/bubbles) to be circular (not a rounded square as appears in the sample attached). Perhaps the words don't need to be in ovals or bound by anything at all; perhaps they do - let's see what you see. We'd like you to choose a font or offer many different fonts you think will capture the practical yet unconventional tone of the book. The book is teaching that managing risks in life is a life-skill that can be learned. The section of the book where this graphic will be placed is called "the power of language" - basically we are saying that thoughts, words and actions create our culture and our destiny. This insight comes from Torvel Pelloru's famous quote:
Carefully watch your thoughts, for they become your words.
Manage and watch your words, for they will become your actions.
Consider and judge your actions, for they have become your habits.
Acknowledge and watch your habits, for they shall become your values.
Understand and embrace your values, for they become your destiny.

Please change the text in the middle of the graphic to say: The Human Culture Cycle

```html
<!DOCTYPE html>
<html lang="en">
<head>
<meta charset="utf-8">
<title>The Human Culture Cycle</title>
<link rel="stylesheet" href="https://fonts.googleapis.com/css2?family=Fredoka:wght@600&display=swap">
<style>
  :root {
    --page: #ffffff;
    --thoughts: #f4cab5;
    --words: #9bc5d6;
    --actions: #d69dbd;
    --habits: #a5c0a5;
    --values: #f06e75;
    --culture: #8ec2c0;
    --hub: #f7f8f9;
    --label: #f3f4f6;
    --title: #f06e75;
  }
  html, body {
    margin: 0;
    width: 1200px;
    height: 1200px;
    overflow: hidden;
    background: var(--page);
  }
  .cycle-diagram {
    display: block;
    width: 1200px;
    height: 1200px;
  }
  .segment-thoughts { fill: var(--thoughts); }
  .segment-words    { fill: var(--words); }
  .segment-actions  { fill: var(--actions); }
  .segment-habits   { fill: var(--habits); }
  .segment-values   { fill: var(--values); }
  .segment-culture  { fill: var(--culture); }
  .hub { fill: var(--hub); }
  .stage-label,
  .cycle-title {
    font-family: "Fredoka", "Varela Round", sans-serif;
    font-weight: 600;
    text-anchor: middle;
    letter-spacing: -0.045em;
  }
  .stage-label {
    font-size: 90px;
    fill: var(--label);
    filter: drop-shadow(2px 3px 1px rgba(90, 70, 80, 0.45));
  }
  .cycle-title {
    font-size: 86px;
    fill: var(--title);
    filter: drop-shadow(2px 3px 1px rgba(90, 60, 70, 0.4));
  }
</style>
</head>
<body>
<svg class="cycle-diagram" viewBox="0 0 1920 1920" role="img" aria-label="The Human Culture Cycle: Thoughts, Words, Actions, Habits, Values, Culture">
  <defs>
    <clipPath id="ring-clip">
      <circle cx="970" cy="922" r="633"/>
    </clipPath>
  </defs>

  <g class="ring" clip-path="url(#ring-clip)">
    <circle class="segment-culture" cx="970" cy="922" r="633"/>
    <polygon class="segment-thoughts"
      points="560,280 630,388 683,470 797,470 742,563 848,733 980,942 1100,723 1185,560 1295,560 1238,460 1283,373 1340,270 1340,-100 560,-100"/>
    <polygon class="segment-words"
      points="980,942 1100,723 1185,560 1295,560 1238,460 1283,373 1340,270 1340,-100 1920,-100 1920,918 1700,918 1603,920 1505,925 1447,1022 1395,928 1227,935"/>
    <polygon class="segment-actions"
      points="980,942 1227,935 1395,928 1447,1022 1505,925 1603,920 1700,918 1920,918 1920,1920 1360,1920 1360,1550 1305,1455 1258,1373 1140,1373 1195,1280 1118,1152"/>
    <polygon class="segment-habits"
      points="980,942 1118,1152 1195,1280 1140,1373 1258,1373 1305,1455 1360,1550 1360,1920 660,1920 660,1570 698,1493 742,1408 685,1307 793,1308 868,1165"/>
    <polygon class="segment-values"
      points="980,942 868,1165 793,1308 685,1307 742,1408 698,1493 660,1570 660,1920 0,1920 0,975 240,975 338,972 435,969 495,868 548,964 733,957"/>
  </g>

  <circle class="hub" cx="980" cy="942" r="247"/>

  <g class="stage-labels">
    <text class="stage-label" x="988" y="532">Thoughts</text>
    <text class="stage-label" x="1382" y="762">Words</text>
    <text class="stage-label" x="1360" y="1178">Actions</text>
    <text class="stage-label" x="982" y="1404">Habits</text>
    <text class="stage-label" x="586" y="1184">Values</text>
    <text class="stage-label" x="570" y="772">Culture</text>
  </g>

  <g class="cycle-titles">
    <text class="cycle-title" x="970" y="830">The</text>
    <text class="cycle-title" x="970" y="921">Human</text>
    <text class="cycle-title" x="970" y="1011">Culture</text>
    <text class="cycle-title" x="970" y="1101">Cycle</text>
  </g>
</svg>
</body>
</html>
```